We need a business card design for our residential home building company based out of East Tennessee and the Smoky Mountains. We have 30 years of experience, and we plan to build homes not only in the state of Tennessee, but out of state as well. We are a different kind of production home builder; we aim to build homes cost-effectively and efficiently but with the character, dignity, and charm of historic homes. Our homes have a timeless style with modern floorplans and features. We would like to see designs that embody a classic style with accents of gold, red, and blue. The resulting business card should convey elegance, strength, character, and trust as well as the careful balance of the old and new.
Motto: "Handcrafting Your Heritage"
Target Market(s)
Adults 40+ from the Northern states looking to settle in Tennessee.
Industry/Entity Type
Residential
Contact Information for Business Card
Birchline Dwellworks, LLC
Marisol Thackett | Director of Operations
24815 Quarrybend Lane | Suite 500
Knoxville, TN 48261
Office: (555)314-2290
Mobile: (555)648-1173
Email: marisol@birchlinedwellworks.example

```html
<!DOCTYPE html>
<html lang="en">
<head>
<meta charset="utf-8">
<title>Birchline Dwellworks, LLC – Business Card</title>
<link rel="stylesheet" href="https://fonts.googleapis.com/css2?family=Cinzel:wght@600&family=Libre+Baskerville&family=Lato:wght@400;700&display=swap">
<style>
  :root {
    --backdrop: #2a2a2a;
    --cream-light: #f7f3ea;
    --cream-dark: #e9e1cf;
    --card-white: #fbfbfb;
    --gold: #7a5f36;
    --red: #d0161c;
    --blue: #3a86c8;
    --ink: #5a5a5a;
  }
  html, body {
    margin: 0;
    width: 1200px;
    height: 997px;
    overflow: hidden;
    background: var(--backdrop);
  }
  .canvas {
    position: relative;
    width: 1200px;
    height: 997px;
  }
  .card {
    position: absolute;
    left: 220px;
    width: 760px;
    height: 434px;
    border-radius: 22px;
    overflow: hidden;
  }
  /* Front face */
  .card-front {
    top: 40px;
    background: linear-gradient(135deg, var(--cream-light), var(--cream-dark));
  }
  .front-brand {
    position: absolute;
    left: 56px;
    bottom: 64px;
    color: var(--gold);
  }
  .front-web {
    font-family: "Libre Baskerville", serif;
    font-size: 14px;
    letter-spacing: 1px;
    margin: 0 0 6px;
  }
  .front-name {
    font-family: "Cinzel", serif;
    font-weight: 600;
    font-size: 42px;
    line-height: 1.05;
    margin: 0 0 10px;
  }
  .front-tagline {
    font-family: "Libre Baskerville", serif;
    font-size: 17px;
    margin: 0;
  }
  /* Back face */
  .card-back {
    top: 523px;
    background: var(--card-white);
  }
  .back-brand {
    position: absolute;
    right: 48px;
    top: 52px;
    font-family: "Cinzel", serif;
    font-weight: 600;
    font-size: 28px;
    line-height: 1.15;
    color: var(--gold);
    text-align: right;
    margin: 0;
  }
  .accent-rule {
    position: absolute;
    height: 3px;
  }
  .rule-red { left: 330px; width: 120px; top: 236px; background: var(--red); }
  .rule-gold { left: 470px; width: 130px; top: 206px; background: var(--gold); }
  .rule-blue { left: 620px; width: 100px; top: 176px; background: var(--blue); }
  .person {
    position: absolute;
    left: 50px;
    top: 232px;
    font-family: "Lato", sans-serif;
  }
  .person-name {
    font-weight: 700;
    font-size: 22px;
    color: var(--gold);
    margin: 0;
  }
  .person-title {
    font-size: 20px;
    color: var(--ink);
    margin: 2px 0 0;
  }
  .address {
    position: absolute;
    right: 48px;
    top: 236px;
    font-family: "Lato", sans-serif;
    font-weight: 700;
    font-size: 16px;
    line-height: 1.4;
    color: var(--gold);
    text-align: right;
    margin: 0;
  }
  .contact-list {
    position: absolute;
    left: 50px;
    top: 318px;
    margin: 0;
    padding: 0;
    list-style: none;
    font-family: "Lato", sans-serif;
    font-size: 18px;
    color: var(--ink);
  }
  .contact-item {
    display: flex;
    align-items: center;
    gap: 14px;
    height: 32px;
  }
  .contact-icon {
    width: 22px;
    height: 22px;
    flex: none;
  }
</style>
</head>
<body>
<main class="canvas">

  <section class="card card-front" aria-label="Business card front">
    <div class="front-brand">
      <p class="front-web">www.birchlinedwellworks.example</p>
      <p class="front-name">Birchline Dwellworks, LLC</p>
      <p class="front-tagline">Homes Cost-Effectively &amp; Efficiently</p>
    </div>
  </section>

  <section class="card card-back" aria-label="Business card back">
    <p class="back-brand">Birchline<br>Dwellworks, LLC</p>

    <span class="accent-rule rule-red"></span>
    <span class="accent-rule rule-gold"></span>
    <span class="accent-rule rule-blue"></span>

    <div class="person">
      <p class="person-name">Marisol Thackett</p>
      <p class="person-title">Director of Operations</p>
    </div>

    <p class="address">24815 Quarrybend Lane,<br>Suite 500 Knoxville, TN 48261</p>

    <ul class="contact-list">
      <li class="contact-item">
        <svg class="contact-icon" viewBox="0 0 22 22" aria-hidden="true">
          <rect width="22" height="22" rx="5" fill="var(--red)"/>
          <path d="M5 8 q6 -5 12 0 l-2 2 l-2 -1 v-1 h-4 v1 l-2 1 z M6 12 h10 v4 h-10 z" fill="#fff"/>
        </svg>
        <span>(555)314-2290</span>
      </li>
      <li class="contact-item">
        <svg class="contact-icon" viewBox="0 0 22 22" aria-hidden="true">
          <rect width="22" height="22" rx="5" fill="var(--gold)"/>
          <rect x="7" y="4" width="8" height="14" rx="1.5" fill="none" stroke="#fff" stroke-width="1.6"/>
        </svg>
        <span>(555)648-1173</span>
      </li>
      <li class="contact-item">
        <svg class="contact-icon" viewBox="0 0 22 22" aria-hidden="true">
          <rect width="22" height="22" rx="5" fill="var(--blue)"/>
          <rect x="4.5" y="6.5" width="13" height="9" fill="none" stroke="#fff" stroke-width="1.4"/>
          <path d="M4.5 6.5 l6.5 5 l6.5 -5" fill="none" stroke="#fff" stroke-width="1.4"/>
        </svg>
        <span>marisol@birchlinedwellworks.example</span>
      </li>
    </ul>
  </section>

</main>
</body>
</html>
```